Webbanner-Design für Online Pfandhaus
Zielgruppe
Online Pfandhaus
Aufgabenstellung
Der Banner für unsere Webseite soll neu gestaltet werden. (Siehe Bilddatei)
Ziel ist es einen schönen, konvertierenden Banner zu gestalten. Der Banner soll sich an die Seite anpassen.
Der Banner wird dann auch für Social Media benötigt.

```html
<!DOCTYPE html>
<html lang="de">
<head>
<meta charset="utf-8">
<title>Leihkontor Nord – Ihr Online-Pfandhaus</title>
<link rel="stylesheet" href="https://fonts.googleapis.com/css2?family=Oswald:wght@500&family=Signika:wght@400;600&family=Open+Sans:wght@600;700&display=swap">
<style>
  :root {
    --brand-blue: #2a3c94;
    --teal: #2f9e9a;
    --chat-green: #35c14c;
    --text-dark: #1c1c1c;
    --text-grey: #555a60;
    --white: #ffffff;
    --badge-red: #d8262b;
  }
  * { margin: 0; padding: 0; box-sizing: border-box; }
  html, body { width: 1200px; height: 889px; overflow: hidden; background: var(--white); }
  body { position: relative; font-family: "Signika", sans-serif; color: var(--text-dark); }

  .site-header { position: absolute; left: 0; top: 0; width: 1200px; height: 74px; background: var(--white); }
  .brand { position: absolute; left: 70px; top: 22px; display: flex; align-items: center; gap: 8px;
    font-family: "Signika", sans-serif; font-weight: 600; font-size: 20px; line-height: 1; color: var(--brand-blue); }
  .brand-dot { width: 24px; height: 24px; border-radius: 50%; background: var(--brand-blue); }
  .main-nav a { position: absolute; top: 24px; font-family: "Oswald", sans-serif; font-weight: 500;
    font-size: 19px; line-height: 1; color: var(--brand-blue); text-decoration: none; white-space: nowrap; }

  .hero { position: absolute; left: 0; top: 74px; width: 1200px; height: 539px;
    background: linear-gradient(180deg, #d9b7a3 0%, #e8c9b2 30%, #d7c4ad 48%, #b89a7a 60%, #a27d5a 80%, #8f6b4a 100%); }
  .hero-band { position: absolute; left: 0; top: 613px; width: 1200px; height: 20px; background: var(--brand-blue); }

  .hero-panel { position: absolute; left: 83px; top: 109px; width: 472px; height: 456px;
    background: rgba(255,255,255,0.72); border-radius: 11px; text-align: center; }
  .hero-panel > * { position: absolute; left: 0; width: 100%; }
  .hero-title { top: 38px; font-family: "Signika", sans-serif; font-weight: 600; font-size: 56px;
    line-height: 1; color: var(--brand-blue); }
  .hero-subtitle { top: 112px; font-size: 40px; line-height: 1; }
  .hero-lead { top: 162px; font-size: 21px; line-height: 34px; }
  .hero-question { top: 248px; font-size: 15px; }
  .request-form { top: 275px; height: 42px; }
  .item-select { position: absolute; left: 116px; top: 0; width: 138px; height: 42px; background: var(--white);
    border-radius: 3px; font-size: 15px; line-height: 42px; text-align: left; padding-left: 13px; }
  .item-select svg { position: absolute; right: 9px; top: 17px; }
  .request-button { position: absolute; left: 265px; top: 0; width: 90px; height: 42px; background: var(--teal);
    color: var(--white); font-size: 16px; line-height: 42px; border-radius: 2px; }
  .hero-alt { top: 333px; font-size: 15px; }
  .hero-alt span { color: var(--chat-green); }
  .membership { top: 374px; height: 52px; }
  .membership p { position: absolute; right: 162px; left: auto; top: 12px; width: 240px;
    font-size: 12px; line-height: 14px; text-align: right; }
  .membership-badge { position: absolute; left: 327px; top: 0; width: 44px; height: 48px; background: var(--badge-red); border-radius: 3px; }

  .hero-products { position: absolute; left: 678px; top: 123px; width: 492px; height: 420px; border-radius: 6px;
    background: linear-gradient(160deg, #3a3a3e 0%, #8ea6bd 25%, #c26a3a 50%, #d8b25a 75%, #7a6a4a 100%); opacity: 0.9; }

  .chat-button { position: absolute; left: 1107px; top: 591px; width: 64px; height: 64px; border-radius: 50%;
    background: var(--chat-green); color: var(--white); font-family: "Open Sans", sans-serif; font-weight: 700;
    font-size: 10px; line-height: 64px; text-align: center; box-shadow: 0 2px 6px rgba(0,0,0,0.25); }

  .benefit { position: absolute; top: 670px; width: 170px; margin-left: -85px; text-align: center; font-family: "Open Sans", sans-serif;
    font-weight: 600; font-size: 18px; line-height: 25px; color: var(--text-grey); }
  .benefit svg { display: block; margin: 0 auto 8px; height: 32px; }

  .how-title { position: absolute; left: 0; width: 1200px; top: 798px; text-align: center; font-family: "Open Sans", sans-serif;
    font-weight: 700; font-size: 38px; color: var(--text-grey); }
  .step-ring { position: absolute; top: 867px; width: 66px; height: 66px; border-radius: 50%; border: 5px solid var(--teal); }
</style>
</head>
<body>
  <header class="site-header">
    <div class="brand"><span class="brand-dot"></span>Leihkontor Nord</div>
    <nav class="main-nav">
      <a style="left:408px">Start</a>
      <a style="left:478px">Anfrage</a>
      <a style="left:567px">Ablauf</a>
      <a style="left:646px">Wissenswertes</a>
      <a style="left:781px">FAQ</a>
      <a style="left:842px">Standorte <svg width="12" height="8" viewBox="0 0 12 8"><path d="M2 2l4 4 4-4" fill="none" stroke="#2a3c94" stroke-width="1.6"/></svg></a>
      <a style="left:964px">Kontakt</a>
      <a style="left:1054px">Über uns</a>
    </nav>
  </header>

  <section class="hero" role="img" aria-label="Unscharfer Ladenhintergrund über einer hellen Holztischplatte"></section>
  <div class="hero-band"></div>

  <div class="hero-panel">
    <h1 class="hero-title">Leihkontor Nord</h1>
    <p class="hero-subtitle">Ihr Online-Pfandhaus</p>
    <p class="hero-lead">Bei uns erhalten Sie in kürzester Zeit Geld fur<br>Ihre Wertgegenstände.</p>
    <p class="hero-question">Weichen Wertgegenstand möchten Sie belehen?</p>
    <div class="request-form">
      <div class="item-select">Schmuck<svg width="12" height="8" viewBox="0 0 12 8"><path d="M1 1l5 5 5-5" fill="none" stroke="#555" stroke-width="1.3"/></svg></div>
      <div class="request-button">Anfrage</div>
    </div>
    <p class="hero-alt">Alternative können Sie uns auch direkt unter <span>Chatwerk</span> kontraktien.</p>
    <div class="membership">
      <p>Wir sind Mitglied im Fachverband<br>Norddeutscher Pfandleiher e.V.</p>
      <div class="membership-badge"></div>
    </div>
  </div>

  <div class="hero-products" role="img" aria-label="Bildschirm, Laptop und Smartphone mit Berglandschaft, davor Goldringe, Goldbarren, ein grüner Edelstein und Armbanduhren"></div>

  <div class="chat-button">Chatwerk</div>

  <div class="benefit" style="left:177px">
    <svg viewBox="0 0 40 26" width="40"><rect x="2" y="2" width="36" height="22" rx="2" fill="none" stroke="#2a3c94" stroke-width="3.5"/><circle cx="20" cy="13" r="6" fill="#2a3c94"/></svg>
    schnelle<br>Auszahlung</div>
  <div class="benefit" style="left:346px">
    <svg viewBox="0 0 40 30" width="40"><path d="M2 6l18-5 18 5-18 6z" fill="#2a3c94"/><path d="M5 11l15 5 15-5v14l-15 5-15-5z" fill="#2a3c94"/></svg>
    versichert bis<br>5000 €</div>
  <div class="benefit" style="left:515px">
    <svg viewBox="0 0 32 32" width="32"><circle cx="16" cy="16" r="13.5" fill="none" stroke="#2a3c94" stroke-width="3"/><path d="M10 16.5l4 4 8-8.5" fill="none" stroke="#2a3c94" stroke-width="3"/></svg>
    keine<br>Bonitätsprüfung</div>
  <div class="benefit" style="left:683px">
    <svg viewBox="0 0 36 30" width="36"><path d="M18 2L2 15h4v13h9v-8h6v8h9V15h4z" fill="#2a3c94"/></svg>
    Abholung von<br>Zuhause</div>
  <div class="benefit" style="left:852px">
    <svg viewBox="0 0 40 30" width="40"><path d="M2 20l10-10h10l-4 5h8l10-10v10L26 26H12l-6 2z" fill="#2a3c94"/></svg>
    100% Diskretion</div>
  <div class="benefit" style="left:1021px">
    <svg viewBox="0 0 32 32" width="32"><circle cx="16" cy="16" r="15" fill="#2a3c94"/><circle cx="11" cy="13" r="2" fill="#fff"/><circle cx="21" cy="13" r="2" fill="#fff"/><path d="M9.5 19q6.5 6 13 0" fill="none" stroke="#fff" stroke-width="2"/></svg>
    Faire Bewertung</div>

  <h2 class="how-title">So funktioniert's:</h2>
  <div class="step-ring" style="left:240px"></div>
  <div class="step-ring" style="left:566px"></div>
  <div class="step-ring" style="left:893px"></div>
</body>
</html>
```